依頼詳細
創業して初めて出す年賀状です。教育委員会や学校の先生、保護者、地域の方など多様な方へ、日頃の御礼と、来年以降の事業への期待を抱いて頂けるようなデザインを希望します。
2色で印刷します。「メイン色:DIC897(青)」、「サブ:おまかせ」の2色を使ったデザインをご提案下さい。
記載項目
1、挨拶文
①Raise up now!
Aim So High We'll Never Be Bored.

②創業して初めての新年を迎えることができました
ひとえに皆々様のご支援の賜物と感謝いたしております
本年も何卒よろしくお願い申し上げます

③Have a great New Year! 2015

それぞれ次の役割をふまえてデザイン下さい。
①はキャッチ、②は小さく、③は適当に。

2、基本情報
(社名)一般社団法人若葉学習協働センター
(代表者名)代表理事 野村 拓

(住所)〒604-0937 京都府京都市中京区竹屋町通柳馬場東入桔梗町218 藤田ビル305
(電話)075-382-9127
(FAX)075-382-9128
希望イメージ
• シンプル
複雑
• 単色
カラフル
• 暗い
明るい
• 日常
高級
• 遊び心
厳粛
• 未来的
伝統的
• 女性的
男性的
希望する色
青系、「メイン色:DIC897(青)」、「サブ:おまかせ」の2色を使って下さい
納品ファイル
• 高解像度JPG (.jpg)
• イラストレーター形式 (.ai)
補足説明
弊団体のロゴデータをお渡ししますので、ロゴを活かしてデザインをご提案下さい
依頼公開後の追記内容
■ 選んだ理由

複数の要素がある中で、当方の依頼意図を汲んで強弱を付けて下さったことが大きな理由です。

■ 提案者全員のお礼・コメント

このたびは多数のご提案を頂戴しまして、誠にありがとうございました。

初めてワークモールを利用しましたが、同じオーダーでここまでバリエーションが出ると想像もしておりませんでした。イラスト作成など個性を活かしたご提案についても御礼申し上げます。

今後ともどうぞよろしくお願い致します。

```html
<!DOCTYPE html>
<html lang="ja">
<head>
<meta charset="utf-8">
<title>若葉学習協働センター 年賀状 2015</title>
<link rel="stylesheet" href="https://fonts.googleapis.com/css2?family=Kaushan+Script&family=Libre+Baskerville:wght@700&family=Noto+Sans+JP:wght@400;500&family=Noto+Serif+JP:wght@500&display=swap">
<style>
  :root {
    --red: #c8102e;
    --red-soft: #d63a52;
    --white: #ffffff;
    --gold: #f6e7a6;
    --navy: #2b4a6b;
    --ink: #333d47;
    --logo-blue: #1f6fa8;
  }
  * { margin: 0; padding: 0; box-sizing: border-box; }
  html, body { width: 813px; height: 1200px; overflow: hidden; background: var(--white); }
  .card { position: relative; width: 813px; height: 1200px; background: var(--white); }
  .greeting-panel {
    position: absolute; left: 0; top: 0; width: 813px; height: 745px;
    background: var(--red); color: var(--white);
  }
  .ship-illustration {
    position: absolute; left: 50px; top: 16px; width: 280px; height: 245px;
  }
  .catch-script {
    position: absolute; left: 395px; top: 170px;
    font-family: "Kaushan Script", cursive; font-size: 66px;
    transform: rotate(-16deg); transform-origin: left bottom; white-space: nowrap;
  }
  .catch-line {
    position: absolute; left: 0; width: 100%; top: 392px; text-align: center;
    font-family: "Libre Baskerville", serif; font-weight: 700; font-size: 37px;
  }
  .message {
    position: absolute; left: 0; width: 100%; top: 488px; text-align: center;
    font-family: "Noto Sans JP", sans-serif; font-size: 24px; line-height: 40px; letter-spacing: 0.04em;
  }
  .new-year {
    position: absolute; left: 0; width: 100%; top: 638px; text-align: center;
    font-family: "Libre Baskerville", serif; font-weight: 700; font-size: 31px; color: var(--gold);
  }
  .org-mark {
    position: absolute; left: 385px; top: 800px; width: 44px; height: 44px;
    border-radius: 50%; background: var(--logo-blue);
  }
  .org-name {
    position: absolute; left: 0; width: 100%; top: 868px; text-align: center;
    font-family: "Noto Serif JP", serif; font-weight: 500; font-size: 40px; color: var(--navy); letter-spacing: 0.04em;
  }
  .representative {
    position: absolute; left: 0; width: 100%; top: 938px; text-align: center;
    font-family: "Noto Sans JP", sans-serif; color: var(--navy);
  }
  .representative .title { font-size: 20px; margin-right: 22px; }
  .representative .name { font-size: 28px; letter-spacing: 0.3em; }
  .contact {
    position: absolute; left: 78px; top: 1006px;
    font-family: "Noto Sans JP", sans-serif; font-size: 21px; line-height: 33px; color: var(--ink);
  }
  .contact .row { display: flex; align-items: center; gap: 8px; }
  .contact svg { width: 22px; height: 22px; flex: none; }
</style>
</head>
<body>
<main class="card">
  <section class="greeting-panel">
    <div class="ship-illustration" role="img" aria-label="白い線で描かれた波間を進む帆船のイラスト">
      <svg width="280" height="245" viewBox="0 0 280 245"><rect width="280" height="245" rx="20" fill="var(--red-soft)"/></svg>
    </div>
    <p class="catch-script">Raise up now!</p>
    <h1 class="catch-line">Aim So High We'll Never Be Bored.</h1>
    <p class="message">創業して初めての新年を迎えることができました<br>ひとえに皆々様のご支援の賜物と感謝いたしております<br>本年も何卒よろしくお願い申し上げます</p>
    <p class="new-year">Have a great New Year! 2015</p>
  </section>

  <div class="org-mark" aria-hidden="true"></div>
  <h2 class="org-name">一般社団法人　若葉学習協働センター</h2>
  <p class="representative"><span class="title">代表理事</span><span class="name">野村 拓</span></p>

  <address class="contact" style="font-style:normal">
    <div>〒604-0937</div>
    <div>京都府京都市中京区竹屋町通柳馬場東入桔梗町218 藤田ビル305</div>
    <div class="row">
      <svg viewBox="0 0 24 24"><rect width="24" height="24" rx="4" fill="var(--red)"/><path d="M8 5l2.5 3-1.5 1.5c.8 2 2.5 3.7 4.5 4.5L15 12.5l3 2.5-1.5 2.5C11 17 7 13 6.5 6.5z" fill="var(--white)"/></svg>
      <span>075-382-9127</span>
    </div>
    <div class="row">
      <svg viewBox="0 0 24 24"><rect width="24" height="24" rx="4" fill="var(--red)"/><rect x="6" y="9" width="12" height="9" fill="var(--white)"/><rect x="8" y="5" width="8" height="5" fill="var(--white)"/></svg>
      <span>075-382-9128</span>
    </div>
  </address>
</main>
</body>
</html>
```